Personal Injury Law Firm in Alaska Needs a Banner Ad Design

Pellmar Law Group is a law firm based in Anchorage, Alaska that specializes in personal injury cases. We are an experienced, professional, and successful legal team that takes pride in always putting the needs of our clients first. Our mission is to secure fair compensation for our clients when they've been injured in an accident or otherwise due to another party's negligence.
We need a banner ad that draws potential clients to our website, where they can call us or submit a description of their case for a free initial consultation. We would like to see designs that are sharp, professional, and sophisticated. The ad should communicate some of our firm's defining qualities: knowledge, experience, compassion, and a strong work ethic.
We need a design that will work for image ads that are vertically oriented (160x600 or similar), horizontally oriented (600x160 or similar), and almost-square (300x250 or similar). Alternatively, we need three different designs that work for each orientation. The general proportions of your designs are more important than specific sizes.
We have included a dropbox file of photos to use as inspiration or incorporate into your design.
Target Market(s)
Victims of vehicular accidents, workplace injury, medical malpractice, etc.
Industry/Entity Type
Law Firm
Look and feel

```html
<!DOCTYPE html>
<html lang="en">
<head>
<meta charset="utf-8">
<title>Pellmar Law Group – We Help Injured Persons</title>
<link rel="stylesheet" href="https://fonts.googleapis.com/css2?family=League+Gothic&family=Lora:ital,wght@0,600;1,500&family=Oswald:wght@400;600&display=swap">
<style>
  :root {
    --navy: #1c3f6c;
    --navy-light: #2c5d93;
    --navy-deep: #15325a;
    --gold: #f6c42f;
    --white: #ffffff;
    --photo-light: #dfe3e6;
    --photo-mid: #9aa7b8;
    --photo-dark: #3c4a66;
  }
  * { margin: 0; padding: 0; box-sizing: border-box; }
  html, body { width: 1200px; height: 320px; overflow: hidden; background: var(--white); }

  .banner {
    position: relative;
    width: 1200px;
    height: 320px;
    overflow: hidden;
  }

  .banner__photo {
    position: absolute;
    inset: 0;
    background:
      radial-gradient(ellipse 240px 200px at 560px 150px, #7b5a4a 0%, rgba(123,90,74,0) 70%),
      radial-gradient(ellipse 220px 260px at 1120px 250px, #9b7466 0%, rgba(155,116,102,0) 70%),
      linear-gradient(90deg, var(--photo-dark) 0%, var(--photo-mid) 45%, var(--photo-light) 75%, #eef0f1 100%);
  }

  .banner__panel {
    position: absolute;
    left: 0;
    top: 0;
    width: 560px;
    height: 320px;
  }

  .headline {
    color: var(--white);
    font-weight: normal;
  }
  .headline > span {
    position: absolute;
    white-space: nowrap;
    line-height: 1;
  }
  .headline__lead {
    left: 120px;
    top: 30px;
    font-family: "Lora", Georgia, serif;
    font-style: italic;
    font-weight: 500;
    font-size: 42px;
  }
  .headline__key {
    left: 118px;
    top: 76px;
    font-family: "League Gothic", "Oswald", sans-serif;
    font-size: 124px;
    color: var(--gold);
    transform: scaleX(0.78);
    transform-origin: left top;
  }
  .headline__tail {
    left: 124px;
    top: 188px;
    font-family: "Oswald", Arial, sans-serif;
    font-weight: 400;
    font-size: 34px;
    letter-spacing: 3px;
  }

  .cta {
    position: absolute;
    left: 120px;
    top: 254px;
    width: 140px;
    height: 46px;
    background: var(--white);
    color: var(--navy-deep);
    font-family: "Oswald", Arial, sans-serif;
    font-weight: 600;
    font-size: 24px;
    line-height: 46px;
    text-align: center;
    text-decoration: none;
  }

  .brand {
    position: absolute;
    left: 632px;
    top: 0;
    width: 388px;
    height: 144px;
    background: var(--white);
    border-bottom: 3px solid var(--navy);
    display: flex;
    flex-direction: column;
    align-items: center;
    justify-content: center;
    gap: 12px;
  }
  .brand__name {
    display: flex;
    align-items: center;
    gap: 14px;
    font-family: "Lora", Georgia, serif;
    font-weight: 600;
    font-size: 32px;
    color: var(--navy);
    white-space: nowrap;
  }
  .brand__square {
    width: 28px;
    height: 28px;
    background: var(--navy);
  }
  .brand__tagline {
    font-family: "Lora", Georgia, serif;
    font-style: italic;
    font-weight: 500;
    font-size: 20px;
    color: var(--navy);
    white-space: nowrap;
  }
</style>
</head>
<body>
  <div class="banner">
    <div class="banner__photo" role="img" aria-label="Photo of a smiling client in a blue sweater talking with a lawyer across a desk in a bright office"></div>

    <svg class="banner__panel" viewBox="0 0 560 320" aria-hidden="true">
      <polygon points="0,0 540,0 450,320 0,320" fill="var(--navy-light)"/>
      <polygon points="0,0 480,0 390,320 0,320" fill="var(--navy)"/>
    </svg>

    <h1 class="headline">
      <span class="headline__lead">We Help</span>
      <span class="headline__key">INJURED</span>
      <span class="headline__tail">PERSONS</span>
    </h1>

    <a class="cta" href="#">Click Here</a>

    <div class="brand">
      <div class="brand__name"><span class="brand__square"></span>Pellmar Law Group</div>
      <div class="brand__tagline">Serving Injured Alaskans Since 2001</div>
    </div>
  </div>
</body>
</html>
```